Larkholm Partners

Need a new website - see more on larkholmpartners.com

Target Market(s)

Finance industry = conservative design

Coding

Coded - Design and coding required

Number of Pages Required

5+ page

Requirements
Should not have
• Dear all,
• Please avoid pictures of people on the website (except the "team" of course :-)

```html
<!DOCTYPE html>
<html lang="en">
<head>
<meta charset="utf-8">
<title>Larkholm Partners</title>
<link href="https://fonts.googleapis.com/css2?family=Source+Sans+3:ital,wght@0,400;0,600;0,700;1,400&display=swap" rel="stylesheet">
<style>
  :root {
    --stage: #000000;
    --ink: #1f1f1f;
    --ink-soft: #4a4a4a;
    --white: #ffffff;
    --accent: #00a8e8;
    --band-grey: #dcdcdc;
    --card-light: #ececec;
    --section-light: #ebebeb;
    --card-dark: #262626;
    --footer: #262626;
    --nav-shade: rgba(30, 32, 36, 0.75);
  }
  * { box-sizing: border-box; margin: 0; padding: 0; }
  html, body {
    width: 1200px; height: 1200px; overflow: hidden;
    background: var(--stage);
    font-family: "Source Sans 3", sans-serif;
  }
  .page {
    position: absolute; left: 293.6px; top: 0;
    width: 768px; height: 1500px;
    transform: scale(0.8); transform-origin: 0 0;
    background: var(--section-light);
    overflow: hidden;
  }
  .abs { position: absolute; }

  /* Hero */
  .hero { left: 0; top: 0; width: 768px; height: 453px;
    background: linear-gradient(90deg, #5b6166 0%, #2a2f38 35%, #1b2230 55%, #3a3f46 80%, #6b7074 100%); }
  .nav { left: 0; top: 0; width: 768px; height: 52px; background: var(--nav-shade); }
  .brand { left: 111px; top: 10px; display: flex; align-items: center; gap: 6px; }
  .brand-mark { width: 33px; height: 33px; border-radius: 50%; background: var(--white); }
  .brand-name { color: var(--white); font-size: 21px; font-weight: 600; letter-spacing: 0.2px; }
  .nav-links { left: 309px; top: 19px; display: flex; gap: 10px; list-style: none; }
  .nav-links li { color: var(--white); font-size: 12.5px; font-weight: 600; }
  .hero-title { left: 103px; top: 176px; color: var(--white); font-size: 38px; font-weight: 700; }
  .hero-lede { left: 105px; top: 222px; width: 330px; color: var(--white);
    font-size: 17px; font-style: italic; line-height: 22.6px; }

  /* Offerings */
  .offer-band { left: 0; top: 453px; width: 768px; height: 325px; background: var(--band-grey); }
  .card { text-align: center; font-size: 12.5px; line-height: 16.8px; color: var(--ink-soft); }
  .card h3 { font-size: 16.5px; font-weight: 400; color: var(--ink); line-height: 21px; margin-bottom: 2px; }
  .card-light { background: var(--card-light); width: 160px; height: 210px; top: 510px; padding: 16px 4px 0; }
  .card-dark { background: var(--card-dark); left: 249px; top: 480px; width: 270px; height: 271px;
    padding: 18px 30px 0; color: var(--white); outline: 1px solid #bdbdbd; }
  .card-dark h3 { color: var(--white); margin-bottom: 5px; }
  .btn { display: block; background: var(--accent); color: var(--white); font-size: 12.5px;
    text-align: center; line-height: 26px; height: 26px; }
  .card .btn { width: 100px; margin: 13px auto 0; }
  .card-dark .btn { margin-top: 10px; }

  /* Features */
  .photo-stairs { left: 98px; top: 812px; width: 285px; height: 192px;
    background: linear-gradient(160deg, #8c8c8c, #6d6d6d 55%, #555 100%); }
  .photo-office { left: 383px; top: 1035px; width: 288px; height: 194px;
    background: linear-gradient(180deg, #8a8a88 0%, #3c4850 35%, #46505a 60%, #8e8c88 100%); }
  .feature h2 { font-size: 22px; font-weight: 600; color: var(--ink); line-height: 24px; }
  .feature p { font-size: 12.5px; line-height: 16.8px; color: var(--ink-soft); width: 215px; margin-top: 2px; }
  .feature .btn { width: 136px; margin-top: 9px; }
  .feature-services { left: 425px; top: 811px; }
  .feature-services .btn { margin-left: 31px; }
  .feature-office { left: 138px; top: 1034px; }
  .feature-office .btn { margin-left: 31px; }

  /* Footer */
  .footer { left: 0; top: 1256px; width: 768px; height: 244px; background: var(--footer); }
  .footer-col { top: 1278px; color: var(--white); }
  .footer-col h4 { font-size: 21px; font-weight: 700; line-height: 26px; }
  .footer-col ul { list-style: none; margin-top: 5px; }
  .footer-col li { font-size: 12.5px; line-height: 17px; }
  .footer-col li::before { content: "›"; color: var(--accent); font-weight: 700; margin-right: 6px; }
  .footer-rule { left: 138px; top: 1370px; width: 135px; height: 1px; background: #4a4a4a; }
</style>
</head>
<body>
<main class="page">
  <header>
    <div class="abs hero" role="img" aria-label="Hero photograph of a business setting with a staircase"></div>
    <div class="abs nav"></div>
    <div class="abs brand"><span class="brand-mark"></span><span class="brand-name">LARKHOLM</span></div>
    <ul class="abs nav-links">
      <li>Home</li><li>Services</li><li>Current Engagements</li><li>News</li><li>Team</li><li>Contact</li>
    </ul>
    <h1 class="abs hero-title">Lorem ipsum</h1>
    <p class="abs hero-lede">dolor sit amet, consectetur adipiscing elit. Integer nec odio. Praesent libero. Sed cursus ante dapibus diam. Sed nisi. Nulla quis sem at nibh elementum imperdiet.</p>
  </header>

  <section>
    <div class="abs offer-band"></div>
    <article class="abs card card-light" style="left:85px;">
      <h3>Private Placements</h3>
      <p>dolor sit amet, consectet ur adipiscing elit. Integer nec odio. Praesent libero. Sed cursus ante dapibus diam. Sed nisi. Nulla quis sem at nibh elementum imperdiet.</p>
      <span class="btn">learn more</span>
    </article>
    <article class="abs card card-dark">
      <h3>Reverse Mergers &amp;<br>Alternative Offerings</h3>
      <p>dolor sit amet, consectetur adipis cing elit. Integer nec odio. Praesent libero. Sed cursus ante dapibus diam. Sed nisi. Nulla quis sem at nibh elementum imperdiet. Duis sagittis ipsum. Praesent mauris. Fusce nec tellus sed augue semp</p>
      <span class="btn">learn more</span>
    </article>
    <article class="abs card card-light" style="left:520px;width:165px;padding-top:13px;">
      <h3 style="letter-spacing:-0.5px;margin-bottom:4px;">Mergers &amp; Acquisitions</h3>
      <p>dolor sit amet, consectet ur adipiscing elit. Integer nec odio. Praesent libero. Sed cursus ante dapibus diam. Sed nisi. Nulla quis sem at nibh elementum imperdiet.</p>
      <span class="btn">learn more</span>
    </article>
  </section>

  <section>
    <div class="abs photo-stairs" role="img" aria-label="Photograph of a concrete staircase"></div>
    <div class="abs feature feature-services">
      <h2>Our Services</h2>
      <p>We offer a wide range of financial services to privately held and publicly traded companies in the United States, Europe and Asia. Though not limited to, Larkholm focuses on the luxury goods sector, primarily taking companies within the high-end consumer</p>
      <span class="btn">View Lorem Ipsum</span>
    </div>
    <div class="abs feature feature-office">
      <h2>Our Office</h2>
      <p>We offer a wide range of financial services to privately held and publicly traded companies in the United States, Europe and Asia. Though not limited to, Larkholm focuses on the luxury goods sector, primarily taking companies within the high-end consumer</p>
      <span class="btn">Contact us</span>
    </div>
    <div class="abs photo-office" role="img" aria-label="Photograph of a modern office interior with a long corridor"></div>
  </section>

  <footer>
    <div class="abs footer"></div>
    <div class="abs footer-col" style="left:138px;"><h4>Lorem Ipsum</h4></div>
    <div class="abs footer-rule"></div>
    <div class="abs footer-col" style="left:343px;">
      <h4>Services</h4>
      <ul><li>dolor sit amet</li><li>consectetur</li><li>adipiscing elit</li><li>Integer nec</li></ul>
    </div>
    <div class="abs footer-col" style="left:534px;">
      <h4>Company</h4>
      <ul><li>odio. Praesent</li><li>libero. Sed</li><li>cursus ante</li><li>dapibus diam</li></ul>
    </div>
  </footer>
</main>
</body>
</html>
```